CD Cover Design for Americana Rock EP Paper Lanterns

We need a CD cover design for an upcoming EP by TW Banfield titled Paper Lanterns. Although the cover should reflect the name of the title track, it should also be consistent with the overall sound of the EP and TW's brand. The EP, however, is a little more rock and a little less Americana that TW's previous EP, Cold Mill Creek.

Please review TW's website at www.twbanfield.net and listen to the attached preview tracks.

```html
<!DOCTYPE html>
<html lang="en">
<head>
<meta charset="utf-8">
<title>Paper Lanterns – TW Banfield</title>
<link href="https://fonts.googleapis.com/css2?family=Arvo:wght@400;700&display=swap" rel="stylesheet">
<style>
  :root {
    --page-bg: #d9d6d2;
    --night-deep: #07080c;
    --night-mid: #2a2f3a;
    --sea-light: #9aa3b3;
    --sea-mid: #4d5563;
    --title-ink: #e9e8ea;
    --title-shadow: rgba(0, 0, 0, 0.85);
    --name-ink: #f3f3f3;
    --url-ink: #c9cbd0;
  }
  * { margin: 0; padding: 0; box-sizing: border-box; }
  html, body {
    width: 1200px;
    height: 926px;
    overflow: hidden;
    background: var(--page-bg);
  }
  .stage {
    width: 1200px;
    height: 926px;
    display: flex;
    align-items: center;
    justify-content: center;
  }
  .cd-cover {
    position: relative;
    width: 860px;
    height: 860px;
    overflow: hidden;
    background: var(--night-deep);
    box-shadow: 0 10px 30px rgba(0, 0, 0, 0.35);
  }
  .cover-photo {
    position: absolute;
    inset: 0;
    background:
      radial-gradient(ellipse 38% 26% at 78% 22%, rgba(200, 206, 218, 0.45), transparent 70%),
      radial-gradient(ellipse 70% 12% at 60% 40%, rgba(220, 226, 236, 0.55), transparent 75%),
      linear-gradient(180deg,
        var(--night-deep) 0%,
        var(--night-mid) 22%,
        #3b4250 34%,
        var(--sea-light) 41%,
        var(--sea-mid) 52%,
        #262a33 72%,
        var(--night-deep) 100%);
  }
  .album-title {
    position: absolute;
    left: 60px;
    top: 56px;
    font-family: "Arvo", serif;
    font-weight: 700;
    font-size: 72px;
    line-height: 1.02;
    letter-spacing: 1px;
    text-transform: uppercase;
    color: var(--title-ink);
    text-shadow: 2px 3px 4px var(--title-shadow);
  }
  .artist-block {
    position: absolute;
    left: 0;
    right: 0;
    bottom: 74px;
    text-align: center;
  }
  .artist-name {
    font-family: "Arvo", serif;
    font-weight: 700;
    font-size: 54px;
    letter-spacing: 12px;
    text-transform: uppercase;
    color: var(--name-ink);
    text-shadow: 1px 2px 3px var(--title-shadow);
  }
  .artist-url {
    margin-top: 10px;
    font-family: "Arvo", serif;
    font-weight: 700;
    font-size: 14px;
    letter-spacing: 5px;
    text-transform: uppercase;
    color: var(--url-ink);
  }
</style>
</head>
<body>
  <main class="stage">
    <section class="cd-cover">
      <div class="cover-photo" role="img" aria-label="Moonlit night seascape: a lone figure walks along a misty rocky shore under a full moon and clouds"></div>
      <h1 class="album-title">Paper<br>Lanterns</h1>
      <div class="artist-block">
        <p class="artist-name">TW Banfield</p>
        <p class="artist-url">www.twbanfield.net</p>
      </div>
    </section>
  </main>
</body>
</html>
```